Stationary for Travel & Tourism Co.
KBR Stationary
Stationary for Travel & Tourism Co. - Travel
Creative Brief
Professional
Tariq Hamdoun Salwi
IT Manager
Office No.627, Noor Plaza Al Hamra Dist. - Prince Fahd Street P.B No.38271 Jeddah 27390 Kingdom of Saudi Arabia
+966 2 6583917 X 482
marwanek@gokbrtrips.com
www.gokbrtrips.com
The horse object in the logo is advised to be nicely embosed as watermark on the stationary particularly on the letter head.

```html
<!DOCTYPE html>
<html lang="en">
<head>
<meta charset="utf-8">
<title>KBR Stationery – Business Card</title>
<link rel="stylesheet" href="https://fonts.googleapis.com/css2?family=Roboto:wght@400;500;700&display=swap">
<style>
  :root {
    --backdrop: #2a2827;
    --card: #f4f4f4;
    --card-edge: #e6e6e6;
    --brand-red: #b3141f;
    --ink-dark: #2b2b2b;
    --ink-grey: #555555;
    --ink-light: #8a8a8a;
    --mark-tint: #e7d3d5;
  }
  * { margin: 0; padding: 0; box-sizing: border-box; }
  html, body {
    width: 1200px; height: 901px; overflow: hidden;
    background: var(--backdrop);
    font-family: "Roboto", Arial, sans-serif;
  }
  .sheet {
    position: relative; width: 1200px; height: 901px;
    display: flex; align-items: center; justify-content: center; gap: 50px;
  }
  .card {
    position: relative; width: 540px; height: 309px;
    background: linear-gradient(160deg, #ffffff 0%, var(--card) 60%, var(--card-edge) 100%);
    border-radius: 22px; overflow: hidden;
    box-shadow: 0 18px 40px rgba(0,0,0,.45);
  }
  /* back side */
  .back-mark {
    position: absolute; left: 18px; top: 30px; width: 260px; height: 230px;
    background: radial-gradient(ellipse at 45% 45%, var(--mark-tint) 0%, rgba(231,211,213,.5) 55%, rgba(231,211,213,0) 75%);
  }
  .back-web {
    position: absolute; right: 40px; bottom: 34px;
    font-size: 12px; letter-spacing: 2.5px; color: var(--ink-grey);
  }
  /* front side */
  .front-mark {
    position: absolute; right: -10px; bottom: -20px; width: 210px; height: 170px;
    background: radial-gradient(ellipse at 50% 50%, var(--mark-tint) 0%, rgba(231,211,213,.45) 55%, rgba(231,211,213,0) 75%);
  }
  .brand { position: absolute; left: 34px; top: 26px; }
  .brand-name {
    display: flex; align-items: center; gap: 10px;
    font-size: 50px; font-weight: 700; color: var(--ink-dark); line-height: 1;
  }
  .brand-square { width: 22px; height: 22px; background: var(--brand-red); }
  .brand-tag {
    margin-top: 6px; font-size: 11px; font-weight: 700;
    color: var(--brand-red); letter-spacing: .6px;
  }
  .address {
    position: absolute; left: 34px; top: 118px;
    font-size: 11.5px; line-height: 14px; color: var(--ink-grey);
  }
  .contacts {
    position: absolute; left: 34px; top: 196px; list-style: none;
    font-size: 11.5px; line-height: 15px; color: var(--ink-grey);
  }
  .contacts li { display: flex; align-items: center; gap: 7px; }
  .contacts svg { width: 11px; height: 11px; fill: var(--brand-red); flex: none; }
  .person { position: absolute; right: 30px; top: 140px; text-align: right; }
  .person-name { font-size: 17px; font-weight: 700; color: var(--brand-red); }
  .person-role { font-size: 11px; color: var(--ink-grey); margin-top: 2px; }
</style>
</head>
<body>
<main class="sheet">
  <section class="card card-back" aria-label="Card back">
    <div class="back-mark" role="img" aria-label="Faint embossed winged horse emblem"></div>
    <p class="back-web">www.gokbrtrips.com</p>
  </section>

  <section class="card card-front" aria-label="Card front">
    <div class="front-mark" role="img" aria-label="Faint embossed winged horse emblem"></div>
    <header class="brand">
      <div class="brand-name"><span class="brand-square"></span>KBR</div>
      <p class="brand-tag">KEY BRIDGE TRAVEL &amp; TOURISM CO</p>
    </header>
    <address class="address" style="font-style:normal">
      Office No.627, Noor Plaza<br>
      Al Hamra Dist. - Prince Fahd Street<br>
      P.B No.38271 Jeddah 27390<br>
      Kingdom of Saudi Arabia
    </address>
    <ul class="contacts">
      <li><svg viewBox="0 0 12 12"><path d="M2 1h3l1 3-1.5 1a7 7 0 0 0 2.5 2.5L8 6l3 1v3a1 1 0 0 1-1 1A9 9 0 0 1 1 2a1 1 0 0 1 1-1z"/></svg>+966 2 6583917 X 482</li>
      <li><svg viewBox="0 0 12 12"><rect x="3" y="0" width="6" height="12" rx="1.2"/></svg>+966 507318246</li>
      <li><svg viewBox="0 0 12 12"><rect x="3" y="0" width="6" height="4"/><rect x="0" y="4" width="12" height="6" rx="1"/></svg>+966 2 6739214</li>
      <li><svg viewBox="0 0 12 12"><path d="M0 2h12v8H0z M0 2l6 5 6-5" /></svg>marwanek@gokbrtrips.com</li>
      <li><svg viewBox="0 0 12 12"><circle cx="6" cy="6" r="6"/></svg>www.gokbrtrips.com</li>
    </ul>
    <div class="person">
      <p class="person-name">Tariq Hamdoun Salwi</p>
      <p class="person-role">IT Manager</p>
    </div>
  </section>
</main>
</body>
</html>
```